Bright Arch Group business card

Bright Arch Group is the parent company of Bright Arch Building, Bright Arch Plumbing and Bright Arch Renovating. We require a sophisticated business card that covers all aspects of the building and plumbing space without using told or construction items.

Industry/Entity Type

Construction Company

Contact Information for Business Card

Gareth Pimley
Director
0472915083
gareth@brightarch.com.au
Www.brightarch.com.au

Font styles to use
Serif
Sans Serif

Colors
3176b5
ffce3e
0692cd
34a7d8
fbee3e
faa54b

Requirements
Must have
• Logo on front
• Logo and details on rear.
Nice to have
• Maybe water mark or shadow effect with logo
Should not have
• Tools or any construction associated items

```html
<!DOCTYPE html>
<html lang="en">
<head>
<meta charset="utf-8">
<title>Bright Arch Group – Business Card</title>
<link href="https://fonts.googleapis.com/css2?family=Arimo:wght@400&display=swap" rel="stylesheet">
<style>
  :root {
    --backdrop: #a5a2a1;
    --water-blue: #3a80bd;
    --water-blue-light: #4a8fc8;
    --water-blue-dark: #3176b5;
    --card-orange: #f7a043;
    --card-orange-light: #faa54b;
    --accent-yellow: #ffce3e;
    --ink: #1c1c22;
    --white: #ffffff;
  }
  * { margin: 0; padding: 0; box-sizing: border-box; }
  html, body {
    width: 1200px;
    height: 546px;
    overflow: hidden;
    background: var(--backdrop);
  }
  .canvas {
    position: relative;
    width: 1200px;
    height: 546px;
  }
  .card {
    position: absolute;
    top: 147px;
    width: 492px;
    height: 282px;
    overflow: hidden;
    background: var(--card-orange);
  }
  .card--front { left: 58px; }
  .card--back { left: 634px; }

  .water-texture {
    position: absolute;
    background: radial-gradient(ellipse at 40% 35%, var(--water-blue-light) 0%, var(--water-blue) 55%, var(--water-blue-dark) 100%);
  }
  .card--front .water-texture { left: 0; top: 0; width: 492px; height: 154px; }
  .card--back .water-texture { left: 0; top: 0; width: 245px; height: 282px; }

  .paper {
    position: absolute;
    background: linear-gradient(160deg, var(--card-orange-light), var(--card-orange));
  }
  .card--front .paper { left: 0; top: 154px; width: 492px; height: 128px; }
  .card--back .paper { left: 245px; top: 0; width: 247px; height: 282px; }

  .accent-shape { position: absolute; }
  .accent-shape polygon { fill: var(--accent-yellow); }

  .wordmark {
    position: absolute;
    display: flex;
    align-items: center;
    justify-content: center;
    font-family: "Arimo", Arial, sans-serif;
    font-weight: 400;
    color: var(--ink);
    line-height: 1;
    white-space: nowrap;
  }
  .wordmark__dot {
    flex: none;
    border-radius: 50%;
    background: var(--card-orange-light);
  }

  .card--front .wordmark { left: 0; width: 492px; top: 68px; font-size: 34px; gap: 12px; }
  .card--front .wordmark__dot { width: 20px; height: 20px; }

  .card--back .wordmark { left: 0; width: 245px; top: 140px; font-size: 21px; gap: 8px; }
  .card--back .wordmark__dot { width: 13px; height: 13px; }

  .slogan {
    position: absolute;
    left: 0;
    top: 198px;
    width: 492px;
    text-align: center;
    font-family: "Arimo", Arial, sans-serif;
    font-size: 14px;
    color: var(--white);
  }

  .contact {
    position: absolute;
    left: 245px;
    top: 0;
    width: 247px;
    height: 282px;
    text-align: center;
    font-family: "Arimo", Arial, sans-serif;
    color: var(--ink);
    white-space: nowrap;
  }
  .contact__name { position: absolute; left: 0; width: 100%; top: 58px; font-size: 17px; }
  .contact__role { position: absolute; left: 0; width: 100%; top: 80px; font-size: 14px; }
  .contact__phone { position: absolute; left: 0; width: 100%; top: 119px; font-size: 18px; }
  .contact__email { position: absolute; left: 0; width: 100%; top: 165px; font-size: 14px; }
  .contact__web { position: absolute; left: 0; width: 100%; top: 211px; font-size: 15px; }
</style>
</head>
<body>
<main class="canvas">

  <section class="card card--front" aria-label="Business card front">
    <div class="water-texture" role="img" aria-label="Blue water droplet texture photograph"></div>
    <div class="paper"></div>
    <svg class="accent-shape" style="left:0;top:154px" width="492" height="21" viewBox="0 0 492 21">
      <polygon points="148,0 342,0 323,21 168,21"/>
    </svg>
    <div class="wordmark">
      <span class="wordmark__dot"></span>
      <span class="wordmark__name">Bright Arch Group</span>
    </div>
    <p class="slogan">salogan goes here</p>
  </section>

  <section class="card card--back" aria-label="Business card back">
    <div class="water-texture" role="img" aria-label="Blue water droplet texture photograph"></div>
    <div class="paper"></div>
    <svg class="accent-shape" style="left:0;top:45px" width="19" height="192" viewBox="0 0 19 192">
      <polygon points="0,0 19,18 19,174 0,192"/>
    </svg>
    <svg class="accent-shape" style="right:0;top:45px" width="20" height="192" viewBox="0 0 20 192">
      <polygon points="20,0 0,22 0,174 20,192"/>
    </svg>
    <div class="wordmark">
      <span class="wordmark__dot"></span>
      <span class="wordmark__name">Bright Arch Group</span>
    </div>
    <div class="contact">
      <p class="contact__name">Gareth Pimley</p>
      <p class="contact__role">Director</p>
      <p class="contact__phone">0472915083</p>
      <p class="contact__email">gareth@brightarch.com.au</p>
      <p class="contact__web">Www.brightarch.com.au</p>
    </div>
  </section>

</main>
</body>
</html>
```